Quill|Marlow & Petrie business card contest

We need a logo for an upscale boutique diversified company involved in real estate, investments, cattle, and more. Our businesses DO NOT need to be reflected in the business card nor do we want them noted. This is our logo and colors and we love our logo and colors. Our logo looks best against a black background and we like to include the firm name in our logo usage. importantly, the names Quill and Marlow are separated by | not / and we use an ampersand not the word and.
On the front of the card, we want to include:
company logo and name (Quill|Marlow & Petrie)
on the back, we would definitely include:
address, email, cell #
logo and name (smaller size than front)

The variable will be location of individual name and title (mine for example is ) - whether on the front OR on the back. interested in variations from which to choose
Dr. Owen T. Caldecott, CFA
Scientifique des Fusées Financières

we would like to use contemporary symbols for address, email address, cell # with an option for web site that we do not intend to use initially. we like two sided cards and believe this design should use four rounded corners with the standard size. we prefer thicker card stock and may look at metal.

```html
<!DOCTYPE html>
<html lang="en">
<head>
<meta charset="utf-8">
<title>Quill|Marlow &amp; Petrie — Business Card</title>
<link rel="stylesheet" href="https://fonts.googleapis.com/css2?family=Bebas+Neue&family=Lato:ital,wght@0,400;0,700;1,400&display=swap">
<style>
  :root {
    --page-bg: #e9e7e4;
    --panel-dark: #5e5e5e;
    --panel-light: #f7f6f5;
    --accent-orange: #d9730f;
    --text-light: #ffffff;
    --text-subtle: #f1f1f1;
    --brand-grey: #555555;
  }
  * { box-sizing: border-box; margin: 0; padding: 0; }
  html, body {
    width: 1200px; height: 900px; overflow: hidden;
    background: var(--page-bg);
  }
  .canvas {
    width: 1200px; height: 900px;
    display: flex; align-items: center; justify-content: center;
  }
  .business-card {
    width: 880px; height: 545px;
    display: flex;
    border-radius: 6px;
    overflow: hidden;
    box-shadow: 0 10px 30px rgba(0,0,0,0.18);
  }
  .card-details {
    width: 429px; height: 100%;
    background: var(--panel-dark);
    color: var(--text-light);
    padding: 64px 0 0 44px;
    position: relative;
  }
  .card-divider { width: 5px; height: 100%; background: var(--accent-orange); }
  .card-brand {
    flex: 1; height: 100%;
    background: var(--panel-light);
    display: flex; align-items: center; justify-content: center;
  }
  .person-name {
    font-family: "Bebas Neue", "Oswald", sans-serif;
    font-size: 38px; letter-spacing: 0.5px; line-height: 1;
  }
  .person-title {
    font-family: "Lato", sans-serif; font-style: italic;
    font-size: 21px; color: var(--text-subtle); margin-top: 4px;
  }
  .contact-list {
    list-style: none;
    position: absolute; left: 44px; top: 296px;
    font-family: "Lato", sans-serif; font-size: 23px; line-height: 32px;
  }
  .contact-item { display: flex; align-items: center; gap: 9px; }
  .contact-icon { width: 18px; height: 18px; fill: var(--text-light); flex: none; }
  .postal-address {
    position: absolute; left: 47px; top: 418px;
    font-family: "Lato", sans-serif; font-style: normal;
    font-size: 23px; line-height: 31px;
  }
  .brand-lockup { display: flex; align-items: center; gap: 12px; }
  .brand-square { width: 16px; height: 16px; background: var(--accent-orange); }
  .brand-name {
    font-family: "Lato", sans-serif; font-weight: 400;
    font-size: 30px; color: var(--brand-grey);
  }
</style>
</head>
<body>
<main class="canvas">
  <article class="business-card">
    <section class="card-details">
      <h1 class="person-name">Dr. Owen T. Caldecott, CFA</h1>
      <p class="person-title">Scientifique des Fusées Financières</p>
      <ul class="contact-list">
        <li class="contact-item">
          <svg class="contact-icon" viewBox="0 0 24 24" aria-hidden="true"><path d="M3 8c0-2 4-4 9-4s9 2 9 4v2h-5V8c-2-.6-6-.6-8 0v2H3zM6 11h12l2 9H4zM12 13a3 3 0 1 0 0 6 3 3 0 0 0 0-6z"/></svg>
          <span>044-987 654 321</span>
        </li>
        <li class="contact-item">
          <svg class="contact-icon" viewBox="0 0 24 24" aria-hidden="true"><path d="M2 5h20v14H2zM4 7v.5l8 6 8-6V7zM4 10v7h16v-7l-8 6z"/></svg>
          <span>info@quillmarlow.com</span>
        </li>
        <li class="contact-item">
          <svg class="contact-icon" viewBox="0 0 24 24" aria-hidden="true"><circle cx="12" cy="12" r="10"/><path d="M7 7c2 0 3 1 3 3s-2 2-2 4 1 3 0 5M15 4c0 2 2 2 3 4s-1 3-2 4 1 4-1 6" fill="none" stroke="#5e5e5e" stroke-width="1.6"/></svg>
          <span>www.quillmarlowpetrie.com</span>
        </li>
      </ul>
      <address class="postal-address">
        421, Address line here,<br>
        45452,Country Name
      </address>
    </section>
    <div class="card-divider"></div>
    <section class="card-brand">
      <div class="brand-lockup">
        <span class="brand-square"></span>
        <span class="brand-name">Quill|Marlow &amp; Petrie</span>
      </div>
    </section>
  </article>
</main>
</body>
</html>
```